Medical Website - (plastic Surgery)

HERE is a "GUIDELINE" of What I need. Please, feel free to ask anything
https://www.filecrate.example/s/k8pwq2mzt/WEBPAGE%20MANUAL.pdf

I need you to design the page, you can do it in english, I'll translate it later. I need at least these pages

homepage
profile
contact me
Main procedures pages (like Breasts) - that has links to specific procedures like breast augmentation
blog

1) Business Name and business logo:
Evandro Tel6ra - Cirurgia Plástica
Logo:
https://www.filecrate.example/s/r3hvx9lqd/Logo%20Gold%204M-V0-FINAL.ai

Fonts
https://www.filecrate.example/sh/t5gnb2wce/AAQr7YuPlKoW3-EzZvHdSaRfN

Personal Pictures (notice that this are my personal pictures, it cannot be copied to use in any other place than my website)
https://www.filecrate.example/sh/w9dkf4hjx/AAPm2-LsQbVe8Nc1-TyGoWzUi

I Have a image stock files, so you can just use some samples and I'll replace them later.

Actual homepage
http://10.47.233.18/evandro-teixeira/index5.html

PSD files for some other pages
https://www.filecrate.example/sh/b2jqz7vnm/AAR-hX482TcLp37KeUwYsDf

2) Navigation Link Name:
www.evandroteixeira.example.br

3) Short Description
I’m a plastic surgeon. I work mostly doing aesthetic surgeries. The website will be use for me as my personal profissional website but keeping in mind that the final objective is to turn my name a “brand" linked to high quality services on plastic surgery.

4) Target Market /Audience:
85% are women, from 20 to 60 y.o.. Mostly of them with good economical condi6on, social class B, AB, A. (Almost all of them are social media connected, use smartphones, and most of them seek and think that plas6c surgery is something glamorous).

5) Webites I like

http://drvolpen.example

clean design, large icons illustrating procedures

http://drvolpen.example/Procedures
how this page organize procedures

http://www.refinedbodyartclinic.example.au
How procedures are organized by pics

http://www.lumenaestheticinstitute.example
Procedures pages
Contact page

Target Market(s)

85% are women, from 20 to 60 y.o.. Mostly of them with good economical condi6on, social class B, AB, A. (Almost all of them are social media connected, use smartphones, and most of them seek and think that plastic surgery is something glamorous).

Industry/Entity Type

Plastic

Font styles to use
Other font styles liked:
• Link already provided to the fonts

Requirements
Must have
• Use pics to illustrate procedures and fonts with enough size to older people read. As well, some people over 40 are not used to internet, so it must be user friendly, intuitive...

```html
<!DOCTYPE html>
<html lang="en">
<head>
<meta charset="utf-8">
<title>Evandro Teixeira – Cirurgia Plástica</title>
<link rel="stylesheet" href="https://fonts.googleapis.com/css2?family=Playfair+Display:ital,wght@0,400;0,700;1,400&family=Open+Sans:wght@400;600;700&display=swap">
<style>
:root{
  --gold:#c4a470;
  --gold-dark:#a8864f;
  --ink:#2b2b2b;
  --text:#4a4a4a;
  --muted:#7a7a7a;
  --light:#f1f0ee;
  --line:#e2ddd4;
  --pink:#d97a9c;
  --blue:#5c82ab;
  --cyan:#2cb1d3;
  --footer:#3a3a3a;
  --footer-dark:#2a2a2a;
  --serif:'Playfair Display', Georgia, serif;
  --sans:'Open Sans', Arial, sans-serif;
}
*{box-sizing:border-box;margin:0;padding:0}
html,body{width:1200px;height:3453px;overflow:hidden;background:#fff}
body{font-family:var(--sans);color:var(--text);position:relative}
.abs{position:absolute}

/* header */
.header{left:0;top:0;width:1200px;height:124px}
.brand{left:50px;top:26px;display:flex;align-items:center;gap:16px}
.brand-mark{width:56px;height:56px;border-radius:50%;background:var(--gold)}
.brand-name{font-family:var(--serif);font-weight:700;font-size:40px;color:var(--ink);line-height:1}
.brand-sub{font-family:var(--serif);font-size:15px;color:var(--gold);letter-spacing:4px;margin-top:6px;text-transform:uppercase}
.call{right:50px;top:8px;text-align:right}
.call-label{font-family:var(--serif);color:var(--gold);font-size:20px}
.call-nums{font-family:var(--serif);font-weight:700;color:var(--ink);font-size:26px;margin-top:2px}
.call-nums span{color:var(--gold);font-weight:400}
.socials{display:flex;gap:8px;justify-content:flex-end;margin-top:10px}
.socials i{display:block;width:30px;height:30px;border-radius:50%;background:var(--gold)}

.nav{left:0;top:124px;width:1200px;height:40px;background:var(--gold);display:flex;align-items:center;padding-left:86px;gap:0}
.nav a{color:#fff;text-decoration:none;font-size:15px;font-weight:600;text-transform:uppercase;padding:0 15px;line-height:40px}
.nav a.active{background:var(--gold-dark)}

/* hero */
.hero{left:0;top:164px;width:1200px;height:426px;background:linear-gradient(90deg,#f3f2f0 0%,#eceae7 45%,#ddd8d2 100%)}
.hero-photo{right:0;top:0;width:720px;height:426px;background:linear-gradient(90deg,rgba(236,233,229,0) 0%,#5a4840 38%,#2a201c 60%,#e8cfc0 82%,#d9b9a6 100%)}
.hero-text{left:50px;top:100px;width:560px}
.hero-title{font-family:var(--serif);font-weight:700;font-size:36px;line-height:1.22;color:var(--ink);text-transform:uppercase}
.hero-copy{font-size:15px;line-height:1.55;color:var(--gold-dark);margin-top:16px}
.btn{display:inline-block;background:var(--gold);color:#fff;font-family:var(--serif);font-weight:700;font-size:15px;border-radius:22px;padding:11px 30px;margin-top:20px}
.dots{left:573px;top:562px;display:flex;gap:7px}
.dots i{width:11px;height:11px;border-radius:50%;background:#bbb}
.dots i:first-child{background:var(--gold)}

/* welcome */
.welcome{left:0;top:590px;width:1200px;height:415px;background:linear-gradient(180deg,#fff 70%,#f4f3f1 100%)}
.doctor{left:100px;top:10px;width:310px;height:405px;background:linear-gradient(180deg,#e7e1db 0%,#d6d3d0 35%,#f4f4f4 60%,#e4e4e4 100%)}
.welcome-text{left:425px;top:60px;width:710px}
.welcome h2{font-family:var(--serif);font-weight:400;font-size:32px;color:var(--ink);text-align:center;text-transform:uppercase}
.welcome .sub{font-family:var(--serif);font-style:italic;color:var(--gold);font-size:18px;text-align:center;margin-top:4px}
.welcome p{font-size:15.5px;line-height:1.62;margin-top:16px;padding-left:0}

/* procedures */
.procs{left:0;top:1005px;width:1200px;height:455px;background:#fff}
.proc{top:50px;width:270px;text-align:center}
.proc svg{display:block;margin:0 auto}
.proc h3{font-family:var(--serif);font-weight:400;font-size:23px;text-transform:uppercase;margin-top:10px}
.proc p{font-size:15px;line-height:1.4;margin-top:8px;color:var(--ink);padding:0 30px}
.proc .more{font-family:var(--serif);font-size:13px;text-transform:uppercase;margin-top:8px;display:block}

/* testimonials */
.testi{left:0;top:1460px;width:1200px;height:495px;background:var(--light);border-top:2px solid var(--line)}
.testi h2{font-family:var(--serif);font-weight:700;font-size:30px;color:var(--gold);text-align:center;margin-top:58px;text-transform:uppercase}
.testi .quote{font-family:var(--serif);font-style:italic;font-size:16px;line-height:1.6;color:var(--text);text-align:center;width:1000px;margin:20px auto 0}
.qmark{left:555px;top:265px;font-family:var(--serif);font-weight:700;font-size:140px;color:var(--gold);line-height:1}
.author{left:470px;top:370px;display:flex;align-items:center;gap:14px}
.avatar{width:100px;height:100px;border-radius:50%;border:4px solid #fff;background:linear-gradient(135deg,#6a4f42,#d7b7a2)}
.author b{font-family:var(--serif);font-size:16px;color:var(--ink);text-transform:uppercase;display:block}
.author span{font-size:14px;color:var(--ink);font-weight:600}

/* news */
.news-title{left:0;top:1985px;width:1200px;text-align:center;font-family:var(--serif);font-size:32px;color:var(--ink);text-transform:uppercase}
.card{left:52px;width:535px;height:200px;border:1px solid var(--line);box-shadow:0 2px 4px rgba(0,0,0,.08);background:#fff}
.card-photo{left:12px;top:12px;width:140px;height:130px;background:linear-gradient(180deg,#6f95b2,#b99b8a 55%,#7aa7c6)}
.card-body{left:168px;top:12px;width:355px}
.card h4{font-family:var(--serif);font-weight:400;font-size:20px;line-height:1.2;color:var(--ink)}
.card .date{font-size:13px;color:var(--gold);margin-top:6px}
.card p{font-size:15px;line-height:1.35;margin-top:6px}
.card .btn{font-size:14px;padding:8px 18px;border-radius:6px;margin-top:10px}
.widget{left:614px;top:2045px;width:538px;height:425px;border:1px solid #c9ccd3;background:#fff;font-size:13px}
.widget-head{background:#eeeff4;border-bottom:1px solid #c9ccd3;padding:6px 10px;font-weight:700;color:#333}
.widget-page{display:flex;gap:10px;padding:10px}
.sq{width:46px;height:46px;background:#3f6fb0}
.widget-post{margin:0 10px;border:1px solid #ddd;padding:10px;display:flex;gap:10px;height:170px}
.widget-post p{line-height:1.45;color:#333}
.widget-fans{padding:10px;color:#555}
.fans{display:grid;grid-template-columns:repeat(9,50px);gap:6px;margin-top:6px}
.fans i{display:block;height:50px;background:linear-gradient(135deg,#8b6d5a,#c8b3a2)}

/* gallery */
.gallery-photo{left:330px;top:2490px;width:540px;height:300px;background:radial-gradient(ellipse at 50% 55%,#e3c3ac 0%,#f2e2d7 35%,#ffffff 70%)}
.gallery-title{left:0;top:2790px;width:1200px;text-align:center;font-family:var(--serif);font-size:28px;color:var(--ink);text-transform:uppercase}
.gallery-line{left:430px;top:2778px;width:340px;height:5px;background:var(--gold)}

.partners{left:0;top:2855px;width:1200px;height:120px}
.partner{top:0;width:300px;text-align:center}
.badge{width:60px;height:60px;margin:0 auto;background:#9aa4ad}
.partner p{font-size:12px;color:var(--ink);margin-top:8px;line-height:1.35}

/* footer */
.footer{left:0;top:3002px;width:1200px;height:338px;background:var(--footer)}
.doc-photo{right:0;top:0;width:290px;height:338px;background:linear-gradient(180deg,#5d8fb0 0%,#9bbdd3 35%,#d1b09b 60%,#4f7fa3 100%)}
.office{top:40px;color:#fff;font-size:14px;line-height:1.5}
.office h5{font-family:var(--serif);color:var(--gold);font-size:17px;text-transform:uppercase;line-height:1.3;margin-bottom:8px}
.office .book{font-family:var(--serif);color:var(--gold);font-weight:700;margin-top:10px}
.foot-brand{left:430px;top:90px;width:340px;text-align:center}
.foot-brand .mark{width:60px;height:60px;border-radius:50%;background:var(--gold);margin:0 auto}
.foot-brand .name{font-family:var(--serif);font-weight:700;font-size:38px;color:#fff;margin-top:12px}
.foot-brand .sub{font-family:var(--serif);color:var(--gold);letter-spacing:4px;font-size:15px;text-transform:uppercase;margin-top:4px}
.foot-brand .socials{justify-content:center;margin-top:22px}
.bottom{left:0;top:3340px;width:1200px;height:113px;background:var(--footer-dark);text-align:center;padding-top:30px}
.bottom nav a{color:var(--gold);font-weight:600;font-size:15px;margin:0 12px;text-decoration:none}
.bottom p{color:#bbb;font-size:14px;margin-top:14px}
</style>
</head>
<body>

<header class="header abs">
  <div class="brand abs">
    <div class="brand-mark"></div>
    <div>
      <div class="brand-name">Evandro Teixeira</div>
      <div class="brand-sub">Cirurgia Plástica</div>
    </div>
  </div>
  <div class="call abs">
    <div class="call-label">Call Us Today</div>
    <div class="call-nums">(47) 9000 1234 <span>/</span> (11) 90000 4321</div>
    <div class="socials"><i></i><i></i><i></i><i></i><i></i><i></i></div>
  </div>
</header>

<nav class="nav abs">
  <a class="active">Home</a><a>Profile</a><a>Face</a><a>Breasts</a><a>Body</a><a>For Men</a><a>Skin</a><a>Blog</a><a>In the Media</a><a>Testimonial</a><a>Contact Us</a>
</nav>

<section class="hero abs">
  <div class="hero-photo abs" role="img" aria-label="Woman with flowing dark hair decorated with flower petals"></div>
  <div class="hero-text abs">
    <h1 class="hero-title">Lorem ipsum dolor sit consectetur adipiscing elit</h1>
    <p class="hero-copy">Lorem ipsum dolor sit amet, consectetur adipiscing elit. Ut sit amet metus ut lorem pharetra venenatis fermentum ut nibh. Nulla aliquet diam eu turpis convallis sit amet malesuada mi ultrices in velit massa.</p>
    <span class="btn">Find Out More</span>
  </div>
  <div class="dots abs" style="top:398px"><i></i><i></i><i></i></div>
</section>

<section class="welcome abs">
  <div class="doctor abs" role="img" aria-label="Surgeon in white coat with stethoscope"></div>
  <div class="welcome-text abs">
    <h2>Welcome</h2>
    <div class="sub">Lorem ipsum dolor sit amet consectetur adipiscing elit</div>
    <p>Lorem ipsum dolor sit amet, consectetur adipiscing elit. Ut sit amet metus ut lorem pharetra venenatis fermentum ut nibh. Nulla aliquet diam eu turpis convallis sit amet malesuada mi ultrices. In in velit massa, vitae condimentum leo. Vivamus nulla sapien, bibendum eget malesuada eget, volutpat nec nisl.</p>
    <p>Aenean turpis magna, dapibus a laoreet a, eleifend eget metus. Vestibulum quis interdum lacus. Donec pharetra luctus euismod. Cum sociis natoque penatibus et magnis dis parturient montes, nascetur ridiculus mus. Sed imperdiet venenatis ante vehicula adipiscing. Pellentesque nisi enim, porta sed malesuada.</p>
  </div>
</section>

<section class="procs abs">
  <div class="proc abs" style="left:40px">
    <svg width="270" height="270" viewBox="0 0 270 270" role="img" aria-label="Portrait of a woman's face for facial procedures">
      <defs><linearGradient id="gFace" x1="0" y1="0" x2="1" y2="1"><stop offset="0" stop-color="#8a6a5c"/><stop offset="1" stop-color="#e9cfc0"/></linearGradient></defs>
      <circle cx="130" cy="130" r="118" fill="url(#gFace)" stroke="#d97a9c" stroke-width="6"/>
      <path d="M175 240 Q240 230 262 170 Q250 250 175 240Z" fill="#d97a9c"/>
    </svg>
    <h3 style="color:var(--pink)">Face</h3>
    <p>Nascetur ridiculus mus sed imperdiet venenatis ante.</p>
    <span class="more" style="color:var(--pink)">Read more</span>
  </div>
  <div class="proc abs" style="left:320px">
    <svg width="270" height="270" viewBox="0 0 270 270" role="img" aria-label="Woman's bare back and shoulders for body procedures">
      <defs><linearGradient id="gBody" x1="0" y1="0" x2="1" y2="1"><stop offset="0" stop-color="#f4efe9"/><stop offset="1" stop-color="#c79a78"/></linearGradient></defs>
      <circle cx="130" cy="130" r="118" fill="url(#gBody)" stroke="#c4a470" stroke-width="6"/>
      <path d="M175 240 Q240 230 262 170 Q250 250 175 240Z" fill="#c4a470"/>
    </svg>
    <h3 style="color:var(--gold)">Corpo</h3>
    <p>Nascetur ridiculus mus sed imperdiet venenatis ante.</p>
    <span class="more" style="color:var(--gold)">Read more</span>
  </div>
  <div class="proc abs" style="left:600px">
    <svg width="270" height="270" viewBox="0 0 270 270" role="img" aria-label="Woman covering her chest for breast procedures">
      <defs><linearGradient id="gBreast" x1="0" y1="0" x2="1" y2="1"><stop offset="0" stop-color="#eae4df"/><stop offset="1" stop-color="#c89f86"/></linearGradient></defs>
      <circle cx="130" cy="130" r="118" fill="url(#gBreast)" stroke="#5c82ab" stroke-width="6"/>
      <path d="M175 240 Q240 230 262 170 Q250 250 175 240Z" fill="#5c82ab"/>
    </svg>
    <h3 style="color:var(--blue)">Mamas</h3>
    <p>Nascetur ridiculus mus sed imperdiet venenatis ante.</p>
    <span class="more" style="color:var(--blue)">Read more</span>
  </div>
  <div class="proc abs" style="left:880px">
    <svg width="270" height="270" viewBox="0 0 270 270" role="img" aria-label="Woman receiving a facial skin treatment">
      <defs><linearGradient id="gSkin" x1="0" y1="0" x2="1" y2="1"><stop offset="0" stop-color="#d8b39b"/><stop offset="1" stop-color="#f6ece6"/></linearGradient></defs>
      <circle cx="130" cy="130" r="118" fill="url(#gSkin)" stroke="#2cb1d3" stroke-width="6"/>
      <path d="M175 240 Q240 230 262 170 Q250 250 175 240Z" fill="#2cb1d3"/>
    </svg>
    <h3 style="color:var(--cyan)">Estetica</h3>
    <p>Nascetur ridiculus mus sed imperdiet venenatis ante.</p>
    <span class="more" style="color:var(--cyan)">Read more</span>
  </div>
</section>

<section class="testi abs">
  <svg class="abs" style="left:570px;top:-2px" width="60" height="32" viewBox="0 0 60 32"><path d="M0 0 L30 30 L60 0Z" fill="#fff"/><path d="M0 1 L30 30 L60 1" fill="none" stroke="#e2ddd4" stroke-width="2"/></svg>
  <h2>Client Testimonials</h2>
  <p class="quote">Maecenas ultrices eros eget justo ultricies in mollis augue commodo. Nullam sem tortor, volutpat non eleifend ut, adipiscing in augue. Aliquam at eros magna. Etiam tempus est quis massa sagittis sit amet lobortis quam malesuada.</p>
  <p class="quote">In interdum blandit ornare. Vivamus malesuada arcu in tellus consectetur rhoncus. Lorem ipsum dolor sit amet, consectetur adipiscing elit. Pellentesque rhoncus magna in tellus luctus gravida. Donec nisl diam, imperdiet eu pulvinar eget, faucibus eu mi. Integer velit erat, blandit a ullamcorper id, volutpat et quam. Cras ornare volutpat nibh sit amet malesuada.</p>
  <svg class="abs" style="left:50px;top:210px" width="30" height="60" viewBox="0 0 30 60"><path d="M26 2 L4 30 L26 58" fill="none" stroke="#c4a470" stroke-width="3"/></svg>
  <svg class="abs" style="left:1120px;top:210px" width="30" height="60" viewBox="0 0 30 60"><path d="M4 2 L26 30 L4 58" fill="none" stroke="#c4a470" stroke-width="3"/></svg>
  <div class="qmark abs">&#8221;</div>
  <div class="author abs">
    <div class="avatar" role="img" aria-label="Client portrait"></div>
    <div><b>Helena Brooks</b><span>Denver, USA</span></div>
  </div>
</section>

<h2 class="news-title abs">Latest News</h2>

<article class="card abs" style="top:2045px">
  <div class="card-photo abs" role="img" aria-label="Surgeon in mask and cap"></div>
  <div class="card-body abs">
    <h4>Lorem ipsum dolor sit amet, consectetur adipiscing ut sit amet metus</h4>
    <div class="date">May 22 2014 by Site Admin</div>
    <p>Lorem ipsum dolor sit amet, consectetur adipiscing elit. Ut sit amet metus ut lorem.</p>
    <span class="btn">Read Full Article</span>
  </div>
</article>
<article class="card abs" style="top:2270px">
  <div class="card-photo abs" role="img" aria-label="Surgeon in mask and cap"></div>
  <div class="card-body abs">
    <h4>Lorem ipsum dolor sit amet, consectetur adipiscing ut sit amet metus</h4>
    <div class="date">May 22 2014 by Site Admin</div>
    <p>Lorem ipsum dolor sit amet, consectetur adipiscing elit. Ut sit amet metus ut lorem.</p>
    <span class="btn">Read Full Article</span>
  </div>
</article>

<aside class="widget abs">
  <div class="widget-head">Find us online</div>
  <div class="widget-page"><div class="sq"></div><div><b>clinica.estetica</b><br>Follow the page</div></div>
  <div class="widget-post">
    <div class="sq"></div>
    <p><b>clinica.estetica</b><br>We recently announced the partner program, a plan that gives new studios free tools and services worth up to $30,000 to help them succeed. Today we are opening the application process for everyone. Learn more here.<br><span style="color:#3f6fb0">May 14 at 10:00am</span></p>
  </div>
  <div class="widget-fans">3,200 people like clinica.estetica
    <div class="fans" role="img" aria-label="Grid of follower thumbnails"><i></i><i></i><i></i><i></i><i></i><i></i><i></i><i></i><i></i><i></i><i></i><i></i><i></i><i></i><i></i><i></i><i></i><i></i></div>
  </div>
</aside>

<div class="gallery-photo abs" role="img" aria-label="Relaxed woman lying on a white towel"></div>
<div class="gallery-line abs"></div>
<h2 class="gallery-title abs">View Our Gallery</h2>

<section class="partners abs">
  <div class="partner abs" style="left:150px"><div class="badge" style="border-radius:50%"></div><p>Associação Nacional de<br>Cirurgia Estética</p></div>
  <div class="partner abs" style="left:450px"><div class="badge"></div><p>Conselho Internacional de<br>Estética Cirúrgica</p></div>
  <div class="partner abs" style="left:750px"><div class="badge"></div><p>Academia Europeia de<br>Medicina Estética</p></div>
</section>

<footer class="footer abs">
  <div class="doc-photo abs" role="img" aria-label="Surgeon wearing mask and cap"></div>
  <div class="office abs" style="left:52px;width:170px">
    <h5>São Paulo /<br>SP Facility</h5>
    Rua das Acácias 410<br>CJ 12<br>Call Us: (11) 90000 4321<br>(11) 3000-1122<br>(11) 3000-3344
    <div class="book">Click Here to Book Online</div>
  </div>
  <div class="office abs" style="left:240px;width:190px">
    <h5>Balneário<br>Camboriú / SC<br>Facility</h5>
    Rua Mar Azul, 220,<br>9 andar SC<br>Call Us: (47) 9000 1234<br>(47) 3000-5566
    <div class="book">Click Here to Book Online</div>
  </div>
  <div class="foot-brand abs">
    <div class="mark"></div>
    <div class="name">Evandro Teixeira</div>
    <div class="sub">Cirurgia Plástica</div>
    <div class="socials"><i></i><i></i><i></i><i></i><i></i><i></i></div>
  </div>
</footer>

<div class="bottom abs">
  <nav><a>Home</a><a>Profile</a><a>Face</a><a>Breasts</a><a>Body</a><a>For Men</a><a>Skin</a><a>Blog</a><a>In the Media</a><a>Testimonial</a><a>Contact Us</a></nav>
  <p>©2014 Evandro Teixeira | Privacy &amp; Disclaimer</p>
</div>

</body>
</html>
```